brix4lane

i want to ues this logo and the same colors used on the business card

cleaning & service

Industry/Entity Type

Business

Contact Information for Business Card

Font styles to use
Serif
Sans Serif
Decorative
Script

Colors
add136
0692cd
000000
5c5c5c
fbfbfb

Requirements
Must have
• cleaning things

```html
<!DOCTYPE html>
<html lang="en">
<head>
<meta charset="utf-8">
<title>brix4lane business card</title>
<link rel="stylesheet" href="https://fonts.googleapis.com/css2?family=Roboto:wght@400;500;700&display=swap">
<style>
  :root {
    --brand-blue: #2761a8;
    --brand-green: #a8cd2f;
    --card-white: #f4f4f4;
    --text-grey: #5c5c5c;
    --divider: #bdbdbd;
    --backdrop: #2b2b2b;
    --paper-white: #ffffff;
  }
  * { margin: 0; padding: 0; box-sizing: border-box; }
  html, body {
    width: 1200px;
    height: 960px;
    overflow: hidden;
    background: var(--backdrop);
    font-family: "Roboto", Arial, sans-serif;
  }
  .canvas {
    position: relative;
    width: 1200px;
    height: 960px;
  }
  .card {
    position: absolute;
    width: 600px;
    height: 343px;
    overflow: hidden;
  }
  .card-front {
    left: 314px;
    top: 113px;
    background: var(--card-white);
  }
  .card-back {
    left: 311px;
    top: 472px;
    background: var(--brand-blue);
  }
  .brand-name {
    position: absolute;
    font-weight: 700;
    font-size: 30px;
    letter-spacing: 0.5px;
    white-space: nowrap;
    transform: translateX(-50%);
  }
  .card-front .brand-name {
    left: 186px;
    top: 148px;
    color: var(--brand-blue);
  }
  .card-back .brand-name {
    left: 300px;
    top: 148px;
    font-size: 34px;
    color: var(--paper-white);
  }
  .divider {
    position: absolute;
    left: 297px;
    top: 92px;
    width: 2px;
    height: 165px;
    background: linear-gradient(to bottom, transparent, var(--divider) 20%, var(--divider) 80%, transparent);
  }
  .holder {
    position: absolute;
    left: 329px;
    top: 106px;
  }
  .holder-name {
    font-size: 20px;
    font-weight: 500;
    color: var(--brand-blue);
    line-height: 24px;
  }
  .holder-role {
    font-size: 14px;
    color: var(--text-grey);
    line-height: 18px;
    margin-top: 2px;
  }
  .contact-list {
    list-style: none;
    margin-top: 26px;
  }
  .contact-item {
    display: flex;
    align-items: center;
    gap: 9px;
    font-size: 14px;
    line-height: 19px;
    color: var(--text-grey);
  }
  .contact-icon {
    width: 13px;
    height: 13px;
    fill: var(--brand-blue);
    flex: none;
  }
  .colour-band {
    position: absolute;
    left: 0;
    bottom: 0;
    width: 600px;
    height: 23px;
  }
  .web-address {
    position: absolute;
    left: 0;
    width: 100%;
    top: 297px;
    text-align: center;
    color: var(--paper-white);
    font-size: 14px;
    letter-spacing: 2px;
  }
</style>
</head>
<body>
<main class="canvas">

  <section class="card card-front">
    <div class="brand-name">brix4lane</div>
    <div class="divider"></div>
    <div class="holder">
      <div class="holder-name">DANIEL REYES</div>
      <div class="holder-role">Owner</div>
      <ul class="contact-list">
        <li class="contact-item">
          <svg class="contact-icon" viewBox="0 0 24 24" aria-hidden="true"><path d="M6.6 10.8a15.1 15.1 0 0 0 6.6 6.6l2.2-2.2a1 1 0 0 1 1-.25 11.4 11.4 0 0 0 3.6.57 1 1 0 0 1 1 1V20a1 1 0 0 1-1 1A17 17 0 0 1 3 4a1 1 0 0 1 1-1h3.5a1 1 0 0 1 1 1c0 1.25.2 2.45.57 3.6a1 1 0 0 1-.25 1z"/></svg>
          <span>555 210 4187</span>
        </li>
        <li class="contact-item">
          <svg class="contact-icon" viewBox="0 0 24 24" aria-hidden="true"><path d="M2 5h20v14H2z M2 5l10 7 10-7" fill="none" stroke="var(--brand-blue)" stroke-width="0"/><path d="M2 5h20v2l-10 6L2 7z M2 9l10 6 10-6v10H2z"/></svg>
          <span>daniel@brix4lane.com</span>
        </li>
        <li class="contact-item">
          <svg class="contact-icon" viewBox="0 0 24 24" aria-hidden="true"><circle cx="12" cy="12" r="10"/><path d="M2 12h20M12 2c3 3 3 17 0 20M12 2c-3 3-3 17 0 20" fill="none" stroke="var(--card-white)" stroke-width="1.6"/></svg>
          <span>www.brix4lane.com</span>
        </li>
      </ul>
    </div>
    <svg class="colour-band" viewBox="0 0 600 23" aria-hidden="true">
      <polygon points="0,0 392,0 386,23 0,23" fill="var(--brand-blue)"/>
      <polygon points="396,0 600,0 600,23 390,23" fill="var(--brand-green)"/>
    </svg>
  </section>

  <section class="card card-back">
    <div class="brand-name">brix4lane</div>
    <div class="web-address">www.brix4lane.com</div>
  </section>

</main>
</body>
</html>
```